Bref créative
business card and letter head
TCW Roofing & Decks, LLC
Corporate
Dale Harrington
Project Manager / Estimator
7426-B Ferncliff
Houston, TX 77094
daleh4182@quorvix.com
Logo for TCW Roofing & Decks, LLC

```html
<!DOCTYPE html>
<html lang="en">
<head>
<meta charset="utf-8">
<title>TCW Roofing &amp; Decks, LLC — Business Card</title>
<link rel="stylesheet" href="https://fonts.googleapis.com/css2?family=Tinos:wght@400;700&display=swap">
<style>
  :root {
    --navy: #0f2f63;
    --paper: #ffffff;
    --ink: #1b2233;
    --backdrop: #e9e6e1;
  }
  * { margin: 0; padding: 0; box-sizing: border-box; }
  html, body { width: 1200px; height: 871px; overflow: hidden; }
  body { background: var(--backdrop); position: relative; font-family: "Tinos", serif; }

  .card {
    position: absolute;
    width: 620px;
    height: 354px;
    box-shadow: 0 10px 28px rgba(0,0,0,0.22);
  }

  .company-name {
    font-family: "Tinos", serif;
    font-weight: 700;
    white-space: nowrap;
  }

  /* Back side */
  .card-back {
    left: 110px; top: 130px;
    background: var(--navy);
    color: var(--paper);
  }
  .card-back .company-name {
    position: absolute;
    left: 0; right: 0; top: 156px;
    text-align: center;
    font-size: 32px;
    line-height: 1;
  }

  /* Front side */
  .card-front {
    left: 470px; top: 390px;
    background: var(--paper);
    color: var(--ink);
    overflow: hidden;
  }
  .card-front .swoosh { position: absolute; right: 0; top: 0; }
  .card-front .company-name {
    position: absolute;
    left: 46px; top: 96px;
    font-size: 28px;
    line-height: 1;
    color: var(--navy);
  }

  .contact { position: absolute; left: 46px; top: 168px; font-size: 16px; line-height: 1.2; }
  .person-name { color: var(--navy); font-weight: 700; font-size: 17px; }
  .person-role { margin-bottom: 12px; }
  .address { margin-bottom: 4px; }
  .line { display: flex; align-items: center; gap: 8px; }
  .line svg { width: 13px; height: 13px; flex: none; fill: var(--navy); }
</style>
</head>
<body>

<section class="card card-back" aria-label="Business card back">
  <div class="company-name">TCW Roofing &amp; Decks, LLC</div>
</section>

<section class="card card-front" aria-label="Business card front">
  <svg class="swoosh" width="620" height="354" viewBox="0 0 620 354" aria-hidden="true">
    <path d="M500 0 C600 80 600 274 500 354 L620 354 L620 0 Z" fill="var(--navy)"/>
    <path d="M462 0 C556 84 556 270 462 354" fill="none" stroke="var(--navy)" stroke-width="11"/>
  </svg>

  <div class="company-name">TCW Roofing &amp; Decks, LLC</div>

  <div class="contact">
    <div class="person-name">Dale Harrington</div>
    <div class="person-role">Project Manager / Estimator</div>
    <div class="address">7426-B Ferncliff<br>Houston, TX 77094</div>
    <div class="line">
      <svg viewBox="0 0 16 16"><path d="M3 1l3 3-2 2c1 2 3 4 5 5l2-2 3 3-2 3C7 15 1 9 1 3z"/></svg>
      <span>713-555-0142</span>
    </div>
    <div class="line">
      <svg viewBox="0 0 16 16"><rect x="4" y="1" width="8" height="14" rx="1.5"/></svg>
      <span>713-555-0187</span>
    </div>
    <div class="line">
      <svg viewBox="0 0 16 16"><rect x="1" y="5" width="14" height="8" rx="1"/><rect x="4" y="2" width="8" height="4"/></svg>
      <span>832-555-0163</span>
    </div>
    <div class="line">
      <svg viewBox="0 0 16 16"><path d="M1 3h14v10H1z M1 3l7 6 7-6" stroke="#fff" stroke-width="1"/></svg>
      <span>daleh4182@quorvix.com</span>
    </div>
  </div>
</section>

</body>
</html>
```